Event Planning Website

We are interested in redesigning our website. We just launched this company and we offer variety of event planning services. We specialize in wedding planning. We offer all inclusive packages, capturing the proposal, wedding planning, day of directing of the event. We help people save money, stay within budget and do the work so they could enjoy their special occasion.

We are looking to design 5 pages (we are open to suggestions to add or remove/combine), we like social media links (Facepage, instagram, yelp, testimonials) incorporated as recommended: Our existing webpage www.tendlanefest.com, Facebook.com/tendlanefest, http://instagram.com/tendlanefest, http://www.yelp.com/biz/tend-lane-fest-san-ramon, logo and flyer are attached. Please let us know if you need additional information. We are looking for a template to be able to easily edit, fill and embed content.

HOME PAGE
This is the landing page, we want it to be informative, attractive, effective leading to contact/lead.

SERVICES
This page should be about our services which we offer (proposal, planning, day of directing), all packages with clean layout detailing the packages.

MEDIA
This page will consist of photo gallery of past events, social media feed, video clips etc.

CONTACT
Modern, hip, minimalistic.

About us
Who we are, the team, bio about each planner within our firm, experience,

Industry/Entity Type

Event Planning

```html
<!DOCTYPE html>
<html lang="en">
<head>
<meta charset="utf-8">
<title>Tend Lane Fest – Planning &amp; Coordination</title>
<link href="https://fonts.googleapis.com/css2?family=Cabin:wght@400;600;700&family=Open+Sans:wght@400;600&family=Pacifico&display=swap" rel="stylesheet">
<style>
:root{
  --page:#efeeee;
  --plum-dark:#442843;
  --plum:#5a3558;
  --lilac:#a988a7;
  --lilac-soft:#b08fae;
  --footer:#ad8aaa;
  --footer-dark:#4b2f48;
  --ink:#222;
  --body:#555;
  --link-blue:#4d57a6;
  --white:#fff;
  --rule:#c9c6c8;
}
*{margin:0;padding:0;box-sizing:border-box}
html,body{width:1200px;height:2564px;overflow:hidden}
body{position:relative;background:var(--page);font-family:"Open Sans",Arial,sans-serif;color:var(--body)}
.abs{position:absolute}

/* header */
.nav-ribbon{left:110px;top:36px}
.nav-link{top:86px;font-family:"Cabin",Arial,sans-serif;font-weight:600;font-size:15px;color:var(--white)}
.brand{left:410px;top:22px;width:380px;height:150px;border-radius:50%;background:#f1e4ee;border:4px solid var(--white);box-shadow:0 0 0 2px var(--lilac),0 4px 10px rgba(0,0,0,.25);display:flex;flex-direction:column;align-items:center;justify-content:center}
.brand-name{font-family:"Cabin",Arial,sans-serif;font-weight:600;font-size:34px;color:var(--plum-dark);letter-spacing:1px;display:flex;align-items:center;gap:12px}
.brand-name::before{content:"";width:18px;height:18px;border-radius:50%;background:var(--plum-dark)}
.brand-tag{font-family:"Cabin",Arial,sans-serif;font-weight:600;font-size:10px;letter-spacing:1px;color:var(--plum-dark);margin-top:2px}

/* slider */
.slider{left:115px;top:145px;width:970px;height:510px;background:var(--white);padding:6px;box-shadow:0 2px 6px rgba(0,0,0,.2)}
.slider-photo{width:100%;height:100%;background:linear-gradient(135deg,#5d6a3e 0%,#c8a887 35%,#e8d2c0 55%,#7a6a86 80%,#3b3a3a 100%)}
.slider-arrow{top:370px;width:32px;height:32px;border-radius:50%;background:var(--white);display:flex;align-items:center;justify-content:center;box-shadow:0 1px 3px rgba(0,0,0,.3)}
.dots{display:flex;gap:7px}
.dot{width:13px;height:13px;border-radius:50%;border:2px solid var(--lilac);background:var(--white)}
.dot.on{background:var(--plum)}
.slider-dots{left:560px;top:630px}

/* services */
.service{top:716px;width:140px;text-align:center}
.service-icon{width:112px;height:112px;margin:0 auto;border-radius:50%;background:var(--lilac);border:5px solid var(--white);box-shadow:0 3px 7px rgba(0,0,0,.3);display:flex;align-items:center;justify-content:center}
.service-label{margin-top:18px;font-family:"Cabin",Arial,sans-serif;font-weight:600;font-size:18px;color:var(--ink)}
.service-dots{left:577px;top:904px}

/* dividers */
.divider{left:390px;width:420px;height:20px}
.divider::before{content:"";position:absolute;left:0;right:0;top:9px;height:1px;background:var(--rule)}
.divider-mark{position:absolute;left:180px;top:2px;width:60px;height:16px;border-radius:8px;background:#8d878b}

/* headings and copy */
.script{font-family:"Pacifico",cursive;color:var(--ink);font-weight:400}
.copy{font-size:12px;line-height:24.5px;color:var(--body)}
.btn{height:37px;display:flex;font-family:"Cabin",Arial,sans-serif;font-size:12px;font-weight:600}
.btn-arrow{width:38px;background:var(--lilac-soft);display:flex;align-items:center;justify-content:center}
.btn-text{width:103px;background:#2a2a2a;color:var(--white);display:flex;align-items:center;padding-left:10px}

.framed{background:var(--white);padding:6px;box-shadow:0 1px 4px rgba(0,0,0,.25)}
.photo{width:100%;height:100%}

/* packages */
.package{top:1401px;width:310px}
.package-photo{height:166px;position:relative;border-bottom:4px solid var(--plum-dark)}
.package-plus{position:absolute;left:137px;bottom:-22px;width:36px;height:36px;border-radius:50%;background:var(--plum-dark);display:flex;align-items:center;justify-content:center}
.package-title{margin-top:22px;font-size:20px}
.package .copy{margin-top:2px;line-height:20.5px}

/* bottom columns */
.col-title{top:1778px;font-size:22px}
.blog-item{left:446px;width:300px;display:flex;gap:12px}
.blog-thumb{width:92px;height:84px;flex:none}
.blog-title{font-family:"Open Sans",Arial,sans-serif;font-weight:600;font-size:12.5px;color:var(--link-blue)}
.blog-item .copy{font-size:11px;line-height:19px}
.nudge{top:1787px;width:20px;height:20px;border-radius:50%;border:1px solid #999;background:var(--white);display:flex;align-items:center;justify-content:center}
.avatar{left:890px;top:1957px;width:84px;height:84px;border-radius:50%;border:4px solid var(--white);background:radial-gradient(circle at 50% 40%,#e8c6a8,#b88d5f);box-shadow:0 1px 4px rgba(0,0,0,.3)}

/* footer */
.footer{left:0;top:2227px;width:1200px;height:231px;background:var(--footer);color:var(--white)}
.footer-title{top:46px;font-family:"Cabin",Arial,sans-serif;font-size:15px;font-weight:400;color:var(--white)}
.footer-text{font-size:10.5px;line-height:17.5px;color:var(--white)}
.footer-list{top:72px;list-style:none;font-size:11.5px;line-height:20px}
.footer-list li{display:flex;align-items:center;gap:10px}
.footer-list .bullet{width:8px;height:8px;border-radius:50%;background:var(--white)}
.news-input{left:855px;top:121px;width:229px;height:33px;background:var(--white);border:none}
.news-btn{left:855px;top:162px;width:116px;height:34px;background:var(--footer-dark);color:var(--white);font-family:"Cabin",Arial,sans-serif;font-size:12px;display:flex;align-items:center;justify-content:center}
.footer-bar{left:0;top:2458px;width:1200px;height:106px;background:var(--footer-dark);color:var(--white);text-align:center}
.footer-links{margin-top:30px;font-size:12px;font-weight:600}
.footer-copy{margin-top:12px;font-size:11px}
</style>
</head>
<body>

<header>
  <svg class="abs nav-ribbon" width="980" height="110" viewBox="0 0 980 110" aria-hidden="true">
    <defs>
      <linearGradient id="ribbonFill" x1="0" y1="0" x2="0" y2="1">
        <stop offset="0" stop-color="#6b3f68"/>
        <stop offset="1" stop-color="#3f2440"/>
      </linearGradient>
    </defs>
    <path d="M0,30 Q490,-4 980,30 L968,100 Q490,78 12,100 Z" fill="url(#ribbonFill)"/>
    <path d="M14,92 Q490,70 966,92" fill="none" stroke="#fff" stroke-width="1.3" stroke-dasharray="4 3" opacity=".8"/>
    <path d="M0,30 Q490,-4 980,30" fill="none" stroke="#9b6aa0" stroke-width="2"/>
  </svg>
  <nav>
    <a class="abs nav-link" style="left:181px">Home</a>
    <a class="abs nav-link" style="left:248px">Services</a>
    <a class="abs nav-link" style="left:329px">Media</a>
    <a class="abs nav-link" style="left:794px">Packages</a>
    <a class="abs nav-link" style="left:881px">Contact</a>
    <a class="abs nav-link" style="left:958px">About Us</a>
  </nav>
  <div class="abs brand">
    <div class="brand-name">TEND LANE FEST</div>
    <div class="brand-tag">PLANNING &amp; COORDINATION</div>
  </div>
</header>

<section class="abs slider">
  <div class="slider-photo" role="img" aria-label="Wedding guests celebrating at an outdoor garden table"></div>
</section>
<div class="abs slider-arrow" style="left:150px"><svg width="12" height="12" viewBox="0 0 12 12"><path d="M8,1 L3,6 L8,11" fill="none" stroke="#333" stroke-width="2"/></svg></div>
<div class="abs slider-arrow" style="left:1018px"><svg width="12" height="12" viewBox="0 0 12 12"><path d="M4,1 L9,6 L4,11" fill="none" stroke="#333" stroke-width="2"/></svg></div>
<div class="abs dots slider-dots"><span class="dot on"></span><span class="dot"></span><span class="dot"></span></div>

<section class="services">
  <div class="abs service" style="left:140px">
    <div class="service-icon"><svg width="52" height="40" viewBox="0 0 52 40"><rect x="2" y="12" width="32" height="22" rx="3" fill="#fff"/><path d="M34,19 L50,11 L50,35 L34,27 Z" fill="#fff"/><circle cx="10" cy="7" r="5" fill="#fff"/><circle cx="24" cy="7" r="5" fill="#fff"/></svg></div>
    <div class="service-label">Video Camera</div>
  </div>
  <div class="abs service" style="left:304px">
    <div class="service-icon"><svg width="48" height="44" viewBox="0 0 48 44"><rect x="8" y="14" width="32" height="10" rx="2" fill="#fff"/><rect x="4" y="26" width="40" height="14" rx="2" fill="#fff"/><path d="M24,11 C18,5 22,1 24,4 C26,1 30,5 24,11 Z" fill="#fff"/></svg></div>
    <div class="service-label">Baker</div>
  </div>
  <div class="abs service" style="left:467px">
    <div class="service-icon"><svg width="44" height="46" viewBox="0 0 44 46"><path d="M4,8 L36,8 L20,26 Z" fill="#fff"/><rect x="19" y="26" width="3" height="14" fill="#fff"/><rect x="11" y="40" width="19" height="3" fill="#fff"/><circle cx="36" cy="8" r="5" fill="none" stroke="#fff" stroke-width="2"/></svg></div>
    <div class="service-label">Bartender</div>
  </div>
  <div class="abs service" style="left:626px">
    <div class="service-icon"><svg width="50" height="40" viewBox="0 0 50 40"><path d="M6,30 Q6,10 25,10 Q44,10 44,30 Z" fill="#fff"/><rect x="2" y="31" width="46" height="4" rx="2" fill="#fff"/><circle cx="25" cy="7" r="3" fill="#fff"/></svg></div>
    <div class="service-label">Caterer</div>
  </div>
  <div class="abs service" style="left:785px">
    <div class="service-icon"><svg width="44" height="44" viewBox="0 0 44 44"><circle cx="29" cy="14" r="10" fill="#fff"/><path d="M23,20 L6,38 L9,41 L27,24" fill="#fff"/></svg></div>
    <div class="service-label">Entertainer</div>
  </div>
  <div class="abs service" style="left:930px">
    <div class="service-icon"><svg width="46" height="46" viewBox="0 0 46 46"><path d="M40,4 C44,2 44,6 42,8 L32,18 L36,38 L32,41 L25,25 L16,33 L17,40 L14,42 L10,34 L3,30 L5,28 L12,29 L20,20 L4,13 L7,10 L28,14 Z" fill="#fff"/></svg></div>
    <div class="service-label">Travel Agent</div>
  </div>
  <div class="abs dots service-dots"><span class="dot on"></span><span class="dot"></span></div>
</section>

<div class="abs divider" style="top:942px"><span class="divider-mark" role="img" aria-label="Scroll flourish"></span></div>

<section class="welcome">
  <h1 class="abs script" style="left:115px;top:978px;font-size:34px">Welcome To Tend Lane Fest</h1>
  <p class="abs copy" style="left:115px;top:1036px;width:545px">Lorem ipsum dolor sit amet, consectetuer adipiscing elit, sed diam nonummy nibh euismod tincidunt ut laoreet dolore magna aliquam erat volutpat. Ut wisi enim ad minim veniam, quis nostrud exerci tation ullamcorper suscipit lobortis nisl ut aliquip ex ea commodo consequat. Lorem ipsum dolor sit amet, consectetuer adipiscing elit, sed diam nonummy nibh euismod tincidunt ut laoreet dolore magna aliquam erat volutpat. Ut wisi enim ad minim veniam, quis nostrud exerci tation ullamcorper suscipit lobortis nisl ut aliquip ex ea commodo consequat. aliquam erat volutpat. Ut wisi enim ad minim veniam,</p>
  <a class="abs btn" style="left:115px;top:1221px"><span class="btn-arrow"><svg width="8" height="12" viewBox="0 0 8 12"><path d="M1,1 L6,6 L1,11" fill="none" stroke="#fff" stroke-width="2"/></svg></span><span class="btn-text">Rearn more</span></a>
  <div class="abs framed" style="left:690px;top:981px;width:395px;height:280px">
    <div class="photo" role="img" aria-label="Bride and groom embracing in a golden meadow" style="background:linear-gradient(120deg,#c9a86e,#e5cf9f 45%,#b88f55)"></div>
  </div>
</section>

<div class="abs divider" style="top:1308px"><span class="divider-mark" role="img" aria-label="Scroll flourish"></span></div>

<section class="packages">
  <h2 class="abs script" style="left:115px;top:1334px;font-size:30px">Packages</h2>
  <article class="abs package" style="left:115px">
    <div class="package-photo" role="img" aria-label="Couple silhouetted against a sunset for the proposal" style="background:linear-gradient(90deg,#2d2016,#8a6a34 45%,#f2d58a 75%,#c09448)"><span class="package-plus"><svg width="14" height="14"><path d="M7,1 V13 M1,7 H13" stroke="#fff" stroke-width="2"/></svg></span></div>
    <h3 class="script package-title">The Proposal</h3>
    <p class="copy">Lorem ipsum dolor sit amet, consectetuer adipiscing elit, sed diam nonummy nibh euismod tincidunt ut laoreet dolore magna aliquam erat volutpat.</p>
  </article>
  <article class="abs package" style="left:444px">
    <div class="package-photo" role="img" aria-label="Smiling couple seated outdoors planning their wedding" style="background:linear-gradient(180deg,#eef2ee,#c9d2c6 55%,#5d6e5a)"><span class="package-plus"><svg width="14" height="14"><path d="M7,1 V13 M1,7 H13" stroke="#fff" stroke-width="2"/></svg></span></div>
    <h3 class="script package-title">The Planning</h3>
    <p class="copy">Lorem ipsum dolor sit amet, consectetuer adipiscing elit, sed diam nonummy nibh euismod tincidunt ut laoreet dolore magna aliquam erat volutpat.</p>
  </article>
  <article class="abs package" style="left:774px">
    <div class="package-photo" role="img" aria-label="Reception stage with two chairs and flowers under lilac lights" style="background:linear-gradient(180deg,#b5aee0,#e4dff2 50%,#9d8b7d)"><span class="package-plus"><svg width="14" height="14"><path d="M7,1 V13 M1,7 H13" stroke="#fff" stroke-width="2"/></svg></span></div>
    <h3 class="script package-title">The Day</h3>
    <p class="copy">Lorem ipsum dolor sit amet, consectetuer adipiscing elit, sed diam nonummy nibh euismod tincidunt ut laoreet dolore magna aliquam erat volutpat.</p>
  </article>
</section>

<div class="abs divider" style="top:1735px"><span class="divider-mark" role="img" aria-label="Scroll flourish"></span></div>

<section class="social">
  <h2 class="abs script col-title" style="left:115px">Socail Media</h2>
  <div class="abs framed" style="left:115px;top:1834px;width:304px;height:191px">
    <div class="photo" role="img" aria-label="Bridal party in yellow dresses on a lawn" style="background:linear-gradient(180deg,#4d86c8,#8ab2d8 40%,#d7b935 60%,#4f7a3a)"></div>
  </div>
  <p class="abs copy" style="left:115px;top:2037px;width:300px">Lorem ipsum dolor sit amet, consectetuer adipiscing elit, sed diam nonummy nibh euismod tincidunt ut laoreet dolore magna aliquam erat volutpat. Ut wisi enim ad minim veniam.</p>
  <a class="abs btn" style="left:115px;top:2146px"><span class="btn-arrow"><svg width="8" height="12" viewBox="0 0 8 12"><path d="M1,1 L6,6 L1,11" fill="none" stroke="#fff" stroke-width="2"/></svg></span><span class="btn-text">Rearn more</span></a>
</section>

<section class="blog">
  <h2 class="abs script col-title" style="left:444px">Blog</h2>
  <div class="abs blog-item" style="top:1832px">
    <div class="blog-thumb" role="img" aria-label="Pink floral centrepiece" style="background:linear-gradient(135deg,#e9c9cf,#c48a98)"></div>
    <div><div class="blog-title">Lorem ipsum dolor sit</div><p class="copy">Lorem ipsum dolor sit amet, consectetuer adipiscing elit, sed diam nonummy nibh euismod tincidunt</p></div>
  </div>
  <div class="abs blog-item" style="top:1928px">
    <div class="blog-thumb" role="img" aria-label="Candlelit table in deep red" style="background:linear-gradient(135deg,#5a1414,#b2462e)"></div>
    <div><div class="blog-title">Lorem ipsum dolor sit</div><p class="copy">Lorem ipsum dolor sit amet, consectetuer adipiscing elit, sed diam nonummy nibh euismod tincidunt</p></div>
  </div>
  <div class="abs blog-item" style="top:2029px">
    <div class="blog-thumb" role="img" aria-label="Reception table with glowing candles" style="background:linear-gradient(135deg,#6a3c3c,#d9b39a)"></div>
    <div><div class="blog-title">Lorem ipsum dolor sit</div><p class="copy">Lorem ipsum dolor sit amet, consectetuer adipiscing elit, sed diam nonummy nibh euismod tincidunt</p></div>
  </div>
</section>

<section class="testimonials">
  <h2 class="abs script col-title" style="left:778px">Testimonials</h2>
  <span class="abs nudge" style="left:1041px"><svg width="6" height="8"><path d="M5,0 L1,4 L5,8" fill="none" stroke="#333" stroke-width="1.5"/></svg></span>
  <span class="abs nudge" style="left:1064px"><svg width="6" height="8"><path d="M1,0 L5,4 L1,8" fill="none" stroke="#333" stroke-width="1.5"/></svg></span>
  <div class="abs framed" style="left:778px;top:1834px;width:304px;height:191px">
    <div class="photo" role="img" aria-label="Couple silhouetted against a purple dusk sky" style="background:linear-gradient(180deg,#4a3a7a,#a86a9a 55%,#f2a47a)"></div>
  </div>
  <div class="abs avatar" role="img" aria-label="Client portrait"></div>
  <p class="abs copy" style="left:778px;top:2037px;width:300px">Lorem ipsum dolor sit amet, consectetuer adipiscing elit, sed diam nonummy nibh euismod tincidunt ut laoreet dolore magna aliquam erat volutpat. Ut wisi enim ad minim veniam.</p>
  <a class="abs btn" style="left:778px;top:2146px"><span class="btn-arrow"><svg width="8" height="12" viewBox="0 0 8 12"><path d="M1,1 L6,6 L1,11" fill="none" stroke="#fff" stroke-width="2"/></svg></span><span class="btn-text">Rearn more</span></a>
</section>

<footer>
  <div class="abs footer">
    <h4 class="abs footer-title" style="left:115px;width:300px;line-height:24px">Make Papper wallets to keep your<br>Coinvault Addresses Safe</h4>
    <p class="abs footer-text" style="left:115px;top:110px;width:305px">Lorem ipsum dolor sit amet, consectetuer adipiscing elit. Vestibulum gravida quam quis nunc rutrum placerat. Proin eu mi vitae neque vel interdum id nec turpis nam auctor faucibus sollicitudin.</p>

    <h4 class="abs footer-title" style="left:477px">Quick Links</h4>
    <ul class="abs footer-list" style="left:479px">
      <li>Wallets</li><li>Buy Rimbo</li><li>News</li><li>Projects</li><li>Contact</li><li>Translate</li>
    </ul>

    <h4 class="abs footer-title" style="left:665px">Social Media</h4>
    <ul class="abs footer-list" style="left:667px;top:68px;line-height:27px">
      <li><span class="bullet"></span>Facepage</li>
      <li><span class="bullet"></span>Chirper</li>
      <li><span class="bullet"></span>Circle Plus</li>
      <li><span class="bullet"></span>ViewTube</li>
    </ul>

    <h4 class="abs footer-title" style="left:851px">Subscribete our newsletter</h4>
    <p class="abs footer-text" style="left:855px;top:76px;width:230px;font-size:11px">Lorem ipsum dolor sit amet dolor consectetur adipiscing elit.</p>
    <input class="abs news-input" type="text" aria-label="Email address">
    <span class="abs news-btn">SUBSCRIBE NOW</span>
  </div>
  <div class="abs footer-bar">
    <p class="footer-links">Price a Wallet&nbsp; / &nbsp;Get Hologram Sticker&nbsp; / &nbsp;Security &amp; Faq&nbsp; / &nbsp;About &amp; Contact&nbsp; / &nbsp;Openfield Lumen</p>
    <p class="footer-copy">Copyright 2015 Tend Lane Fest. All Rights Reserved.</p>
  </div>
</footer>

</body>
</html>
```